International Lifestyle Real Estate Brokerage Needs Eye Catching Website

We need a new website for a cutting edge / dynamic real estate startup, Pinecrest Realty, that will serve as a concierge brokerage to assist cold weather residents with the research, selection, financing and purchase of vacation / retirement properties in warm weather climates in the US and then globally. We will have personally vetted all properties to insure that our clients are only getting the best of the best with no hidden surprises.

** The website design will ultimately need to be coded into a wordpress theme.

We are not locked into any specific colour scheme but would prefer something warm vs cold as that is really the lifestyle we are selling. We like lots of white negative space and hope to allow high end photography to provide most of the pop in colour.

I have attached mock up wire frames to demonstrate desired functionality for three pages we need designed

1) Home Page
2) Market Profile (City overview and developments)
3) Community Profile Page (Individual development profile)

I have also included .ai file for the logo. Not locked into red.

Final design should communicate excitement, lifestyle while maintaining an air of professionalism and reliability. We have developed over 30 sites and have high expectations for the winning design.

Regards,
Dan
Updates

Project Deadline Extended Reason: Hello,I have been called away from this project for the past couple of weeks and have been unable to get together with the people involved to get a consensus on direction forward. Apologies for the delay - we are still very much committed to moving forward.Regards,Dan Added Wednesday, July 6, 2016

Target Market(s)

Canadian and Northern US residents looking to purchase vacation or retirement real estate in warmer climates, initially in the US, but eventually Internationally.

Industry/Entity Type

Real Estate

Contact Information for Business Card

Names for Business Cards

Dan Whitford
705.555.2147
dan@pinecrestrealty-example.ca

Coding

Coded - Design and coding required

Number of Pages Required

3 page

Font styles to use
Serif
Sans Serif

Requirements
Must have
• See wireframe documents uploaded.
• Site design will ultimately be coded into a child theme to function on a selected wordpress theme. If the designer has a Wordpres Theme in mind that would be compatible with the design we would appreciate that information.
Nice to have
• See wireframe documents uploaded. Prefer clean, modern site, white negative space, bold photography will add most of the colour and pop.
Should not have
• Anything cartoony or sophmoric.

```html
<!DOCTYPE html>
<html lang="en">
<head>
<meta charset="utf-8">
<title>Pinecrest Realty — Home</title>
<link rel="stylesheet" href="https://fonts.googleapis.com/css2?family=Teko:wght@400;500;600&family=Open+Sans:wght@400;600;700&display=swap">
<style>
:root{
  --red:#d33a3a;
  --dark:#333333;
  --darker:#222222;
  --footer-bottom:#141414;
  --light:#f4f4f4;
  --mid:#ededed;
  --text:#555555;
  --muted:#777777;
  --white:#ffffff;
  --head:#3a3a3a;
}
*{box-sizing:border-box;margin:0;padding:0}
html,body{width:1200px;height:3152px;overflow:hidden}
body{font-family:"Open Sans",Arial,sans-serif;color:var(--text);background:var(--white);position:relative}
.display{font-family:"Teko","Oswald",sans-serif;text-transform:uppercase;letter-spacing:.5px}
section,header,footer{position:absolute;left:0;width:1200px}

/* hero */
.hero{top:0;height:555px;background:linear-gradient(180deg,#5f9fd8 0%,#a9cbe6 30%,#d9e6ea 40%,#7fae3c 52%,#5e9128 75%,#3f6b1e 100%)}
.brand{position:absolute;left:98px;top:58px;color:var(--white);text-align:center}
.brand .mark{display:block;width:14px;height:14px;border-radius:50%;background:var(--white);margin:0 auto 10px}
.brand .name{font-family:"Teko",sans-serif;font-size:30px;letter-spacing:3px;line-height:1}
.brand .sub{font-family:"Teko",sans-serif;font-size:16px;letter-spacing:4px;line-height:1}
.nav{position:absolute;right:98px;top:48px;display:flex;gap:26px;align-items:center}
.nav a{font-family:"Teko",sans-serif;color:var(--white);text-decoration:none;font-size:17px;letter-spacing:.5px;display:flex;align-items:center;gap:8px}
.nav a.register{border:2px solid var(--white);border-radius:3px;padding:4px 18px 2px}
.hero-copy{position:absolute;top:365px;left:0;width:1200px;text-align:center;color:var(--white)}
.hero-copy h1{font-family:"Teko",sans-serif;font-weight:500;font-size:68px;line-height:1;letter-spacing:1px;color:#f4f0e6;text-shadow:0 0 2px #333,0 2px 4px rgba(0,0,0,.5)}
.hero-copy p{font-family:"Teko",sans-serif;font-size:21px;letter-spacing:.5px;margin-top:2px;text-transform:uppercase}
.dots{display:flex;justify-content:center;gap:7px}
.dots span{width:14px;height:14px;border-radius:50%;border:2px solid var(--white)}
.dots span.on{background:var(--white)}
.hero .dots{position:absolute;top:490px;left:0;width:1200px}

.search-band{top:555px;height:93px;background:#2a2e24}
.search{position:absolute;left:242px;top:23px;display:flex}
.search .field{width:603px;height:47px;background:var(--white);font-size:13px;color:#888;padding:15px 18px}
.search .go{width:113px;height:47px;background:var(--red);color:var(--white);font-family:"Teko",sans-serif;font-size:22px;text-align:center;padding-top:10px}

/* welcome */
.welcome{top:648px;height:332px;background:var(--light);text-align:center}
.section-title{font-family:"Teko",sans-serif;font-weight:500;font-size:40px;color:var(--head);text-transform:uppercase;letter-spacing:.5px;line-height:1}
.welcome .section-title{margin-top:62px}
.welcome p{width:880px;margin:20px auto 0;font-size:12.5px;line-height:22px;color:var(--text)}
.btns{display:flex;justify-content:center;gap:10px;margin-top:28px}
.btn{display:inline-block;width:158px;height:42px;color:var(--white);font-size:17px;padding-top:10px;text-transform:uppercase;font-weight:600}
.btn.dark{background:#555}
.btn.red{background:var(--red)}

/* developments */
.dev-head{top:980px;height:130px;background:var(--white);text-align:center}
.dev-head .section-title{margin-top:30px}
.dev-head p{font-size:15px;color:var(--text);margin-top:8px}
.dev-body{top:1110px;height:530px;background:var(--mid)}
.dev-cards{position:absolute;top:80px;left:100px;display:flex;gap:32px}
.dev-card{width:310px;height:322px;position:relative;border:3px solid var(--white);box-shadow:0 1px 3px rgba(0,0,0,.15)}
.photo{display:block;width:100%;height:100%}
.dev-card .cap{position:absolute;left:0;bottom:0;width:100%;height:96px;background:rgba(30,45,25,.82);color:var(--white);text-align:center;padding-top:14px}
.dev-card .cap h3{font-family:"Teko",sans-serif;font-weight:500;font-size:19px;letter-spacing:.5px}
.dev-card .cap p{font-size:11.5px;line-height:17px;margin-top:4px;padding:0 20px}
.dev-body .dots{position:absolute;top:456px;left:0;width:1200px}
.dev-body .dots span{border-color:#bbb;border-width:1px}
.dev-body .dots span.on{background:var(--red);border-color:var(--red)}

/* markets */
.markets{top:1640px;height:685px;background:var(--white);text-align:center}
.markets .section-title{margin-top:48px}
.tabs{display:flex;justify-content:center;margin-top:26px}
.tabs span{display:block;width:155px;height:44px;font-size:15px;padding-top:12px;border-bottom:2px solid #ddd;color:#444}
.tabs span.on{background:var(--red);color:var(--white);border-color:var(--red)}
.grid{position:absolute;top:178px;left:98px;display:grid;grid-template-columns:repeat(3,332px);grid-auto-rows:225px;gap:3px}
.tile{position:relative}
.tile .label{position:absolute;left:0;bottom:0;width:100%;height:38px;background:rgba(0,0,0,.55);color:var(--white);font-size:15px;font-weight:700;padding-top:9px;text-transform:uppercase}
.tile.info{background:#3c3c3c;color:var(--white);padding:30px 36px 0}
.tile.info h3{font-family:"Teko",sans-serif;font-weight:500;font-size:25px;text-transform:uppercase}
.tile.info p{font-size:11.5px;line-height:19px;margin-top:6px}
.tile.info .more{display:inline-block;margin-top:16px;border:1px solid #ccc;padding:6px 12px;font-size:11px;text-transform:uppercase}

/* blog */
.blog{top:2325px;height:475px;background:var(--light)}
.blog .section-title{text-align:center;margin-top:50px}
.posts{position:absolute;top:127px;left:98px;display:flex;gap:42px}
.post{width:310px;border-bottom:1px solid #ddd;height:290px}
.post .photo{height:153px}
.post h4{font-size:15px;font-weight:400;color:#444;margin-top:18px}
.post .meta{font-size:12.5px;color:var(--muted);margin-top:10px;display:flex;align-items:center;gap:6px}
.post p{font-size:12px;line-height:21px;color:var(--muted);margin-top:10px}

/* footer */
.site-footer{top:2800px;height:295px;background:var(--darker);color:#ddd}
.col{position:absolute;top:40px}
.col h5{font-family:"Teko",sans-serif;font-weight:500;font-size:23px;color:var(--white);text-transform:uppercase;letter-spacing:.5px}
.f-brand{left:98px}
.f-brand .brand{position:static;display:inline-block;margin-bottom:20px}
.f-line{display:flex;gap:12px;font-size:13.5px;line-height:22px;margin-bottom:8px;align-items:flex-start}
.f-line svg{flex:none;margin-top:3px}
.f-map{left:390px}
.map{width:262px;height:152px;margin-top:14px;background:linear-gradient(135deg,#d8d8d8,#bdbdbd);border:4px solid var(--white)}
.f-news{left:705px;width:250px}
.f-news p{font-size:11.5px;line-height:19px;margin-top:12px}
.f-news .input{width:245px;height:40px;background:var(--white);color:#777;font-size:11px;padding:13px 14px;margin-top:18px}
.f-news .sub{display:inline-block;background:var(--red);color:var(--white);font-size:11px;font-weight:700;padding:12px 16px;margin-top:12px}
.f-links{left:1002px}
.f-links ul{list-style:none;margin-top:10px}
.f-links li{font-size:12px;line-height:23.5px;display:flex;align-items:center;gap:10px}
.f-links li::before{content:"";border-left:6px solid #ddd;border-top:4px solid transparent;border-bottom:4px solid transparent}
.footer-bottom{top:3095px;height:57px;background:var(--footer-bottom);color:#ccc;font-size:12px}
.footer-bottom .copy{position:absolute;left:98px;top:20px}
.social{position:absolute;right:110px;top:14px;display:flex;gap:8px}
.social span{width:28px;height:28px;border-radius:50%;background:var(--white)}
</style>
</head>
<body>

<header class="hero">
  <div class="photo" role="img" aria-label="Sunny golf course green by the ocean with palm trees and a flag pin" style="position:absolute;inset:0"></div>
  <div class="brand">
    <span class="mark"></span>
    <div class="name">PINECREST</div>
    <div class="sub">REALTY</div>
  </div>
  <nav class="nav">
    <a href="#"><svg width="16" height="14" viewBox="0 0 16 14"><path d="M8 14L1.5 7.5A4 4 0 0 1 8 2.5 4 4 0 0 1 14.5 7.5Z" fill="#fff"/></svg>SAVED</a>
    <a href="#">SEARCH</a>
    <a href="#">ABOUT</a>
    <a href="#">CONTACT</a>
    <a href="#">LOGIN</a>
    <a href="#" class="register">REGISTER</a>
  </nav>
  <div class="hero-copy">
    <h1>LIFE IS TOO SHORT TO BE COLD</h1>
    <p>Helping fellow Canadians purchase their dream vacation home in the sun</p>
  </div>
  <div class="dots"><span class="on"></span><span></span><span></span><span></span></div>
</header>

<section class="search-band">
  <div class="search">
    <div class="field">Where shall we look?</div>
    <div class="go">LET'S GO!</div>
  </div>
</section>

<section class="welcome">
  <h2 class="section-title">Welcome to Pinecrest Realty</h2>
  <p>We guide northern families through every step of finding a warm weather home, from first research and careful selection to financing and closing. Every property we present has been personally visited and vetted by our team, so you can buy with confidence and without surprises. Tell us where the sun calls you and we will handle the rest.</p>
  <div class="btns"><span class="btn dark">Learn More</span><span class="btn red">Register</span></div>
</section>

<section class="dev-head">
  <h2 class="section-title">Featured Developments</h2>
  <p>Handpicked communities in the sunniest places to live</p>
</section>

<section class="dev-body">
  <div class="dev-cards">
    <article class="dev-card">
      <div class="photo" role="img" aria-label="Green two-storey house with white porch" style="background:linear-gradient(180deg,#7fb2e6,#9aa86a 55%,#5d7a3a)"></div>
      <div class="cap"><h3>Palm Grove Estates</h3><p>Quiet streets, mature trees and easy access to the beach</p></div>
    </article>
    <article class="dev-card">
      <div class="photo" role="img" aria-label="Craftsman style family home with covered porch" style="background:linear-gradient(180deg,#4e8fdb,#b7a98d 55%,#5f7a44)"></div>
      <div class="cap"><h3>Harbour Point Village</h3><p>Modern craftsman homes steps from the marina and shops</p></div>
    </article>
    <article class="dev-card">
      <div class="photo" role="img" aria-label="Cream stucco house with flowering garden" style="background:linear-gradient(180deg,#8ab8e8,#d8cbb0 55%,#6d8a42)"></div>
      <div class="cap"><h3>Sunset Ridge Homes</h3><p>Spacious lots, bright gardens and golf course views</p></div>
    </article>
  </div>
  <div class="dots"><span class="on"></span><span></span><span></span></div>
</section>

<section class="markets">
  <h2 class="section-title">Featured Markets</h2>
  <div class="tabs"><span class="on">UNITED STATES</span><span>MEXICO</span><span>SOUTH AMERICA</span></div>
  <div class="grid">
    <div class="tile"><div class="photo" role="img" aria-label="Modern villa with pool at dusk" style="background:linear-gradient(180deg,#9cc0e0,#c9b79a 55%,#4f8fa8)"></div><div class="label">Orlando</div></div>
    <div class="tile"><div class="photo" role="img" aria-label="Timber and stone home with lawn" style="background:linear-gradient(180deg,#6fa2dc,#9d8f7a 55%,#5e8a3a)"></div><div class="label">Naples</div></div>
    <div class="tile"><div class="photo" role="img" aria-label="Large suburban home with trees" style="background:linear-gradient(180deg,#5b96dc,#b4ad9c 55%,#5a8436)"></div><div class="label">Fort Meyers</div></div>
    <div class="tile"><div class="photo" role="img" aria-label="Lit contemporary home in the evening" style="background:linear-gradient(180deg,#3d5a7c,#8a7a66 55%,#2f4a5c)"></div><div class="label">Clearwater</div></div>
    <div class="tile"><div class="photo" role="img" aria-label="Blue clapboard house with tree" style="background:linear-gradient(180deg,#7aaee2,#8a98a8 55%,#5a8a3a)"></div><div class="label">Asheville</div></div>
    <div class="tile info">
      <h3>Featured Markets</h3>
      <p>Explore the warm weather cities our clients love most, with local guides, price trends and vetted communities in each market.</p>
      <span class="more">Read more &#9656;</span>
    </div>
  </div>
</section>

<section class="blog">
  <h2 class="section-title">Recent Blog</h2>
  <div class="posts">
    <article class="post">
      <div class="photo" role="img" aria-label="Colourful waterfront town" style="background:linear-gradient(180deg,#7fb0dc,#d69a5a 55%,#3d6f8f)"></div>
      <h4>Buying abroad made simple</h4>
      <div class="meta"><svg width="12" height="12" viewBox="0 0 12 12"><circle cx="6" cy="6" r="5" fill="none" stroke="#777" stroke-width="1.5"/><path d="M6 3v3h2.5" stroke="#777" stroke-width="1.3" fill="none"/></svg>3 minutes ago, 0 comments</div>
      <p>A short guide to the paperwork, timelines and costs you should expect when buying a home outside Canada.</p>
    </article>
    <article class="post">
      <div class="photo" role="img" aria-label="City skyline over water" style="background:linear-gradient(180deg,#6aa6e0,#9fb4c8 55%,#3b6a8a)"></div>
      <h4>Top markets for retirees</h4>
      <div class="meta"><svg width="12" height="12" viewBox="0 0 12 12"><circle cx="6" cy="6" r="5" fill="none" stroke="#777" stroke-width="1.5"/><path d="M6 3v3h2.5" stroke="#777" stroke-width="1.3" fill="none"/></svg>3 minutes ago, 0 comments</div>
      <p>We compare climate, healthcare and cost of living in the cities our winter clients ask about most often.</p>
    </article>
    <article class="post">
      <div class="photo" role="img" aria-label="Couple meeting an agent outside a house" style="background:linear-gradient(180deg,#9cc7a0,#c9b9a2 55%,#6f8f5a)"></div>
      <h4>Financing your sun home</h4>
      <div class="meta"><svg width="12" height="12" viewBox="0 0 12 12"><circle cx="6" cy="6" r="5" fill="none" stroke="#777" stroke-width="1.5"/><path d="M6 3v3h2.5" stroke="#777" stroke-width="1.3" fill="none"/></svg>3 minutes ago, 0 comments</div>
      <p>How cross border mortgages work and what lenders look for when you buy a second home in the south.</p>
    </article>
  </div>
</section>

<footer class="site-footer">
  <div class="col f-brand">
    <div class="brand"><span class="mark"></span><div class="name">PINECREST</div><div class="sub">REALTY</div></div>
    <div class="f-line"><svg width="14" height="18" viewBox="0 0 14 18"><path d="M7 17S1 10 1 6.5a6 6 0 0 1 12 0C13 10 7 17 7 17Z" fill="none" stroke="#ddd" stroke-width="1.5"/><circle cx="7" cy="6.5" r="2" fill="#ddd"/></svg><span>Pinecrest Realty, Level 2|48 Harbour<br>Lane|Maple Bay<br>ON 1042</span></div>
    <div class="f-line"><svg width="14" height="14" viewBox="0 0 14 14"><path d="M3 1l3 3-2 2a8 8 0 0 0 4 4l2-2 3 3-2 2C6 13 1 8 1 3Z" fill="#ddd"/></svg><span>Phone : 1300 555 018</span></div>
    <div class="f-line"><svg width="15" height="11" viewBox="0 0 15 11"><rect x=".75" y=".75" width="13.5" height="9.5" fill="none" stroke="#ddd" stroke-width="1.5"/><path d="M1 1l6.5 5L14 1" fill="none" stroke="#ddd" stroke-width="1.5"/></svg><span>support@pinecrestrealty-example.com</span></div>
  </div>
  <div class="col f-map">
    <h5>Our Location</h5>
    <div class="map" role="img" aria-label="Street map of the office location"></div>
  </div>
  <div class="col f-news">
    <h5>Join Our Newsletter</h5>
    <p>Get new listings and market news sent to your inbox each month</p>
    <div class="input">Enter Name</div>
    <span class="sub">SUBSCRIBE</span>
  </div>
  <div class="col f-links">
    <h5>Quick Links</h5>
    <ul><li>About</li><li>OUR PROCESS</li><li>RESOURCES</li><li>REGISTER</li><li>CONTACT</li><li>LOGIN</li><li>SAVED</li></ul>
  </div>
</footer>

<footer class="footer-bottom">
  <div class="copy">Copyright 2016 | All Rights Reserved - Pinecrest Realty</div>
  <div class="social"><span></span><span></span><span></span><span></span></div>
</footer>

</body>
</html>
```